Enlargement project

We would like to create an enlargement of the attached business card design, so that we are able to print hi-res business cards from it,

The end result we are after is an illustrator template that contains hi-res graphics and text that we can edit to insert people's names, job titles, phone and email details

The two colours used within the design are:

Pantone 350 (green)
Panton 484 (red)

The fonts used are;

Futura Medium
Futura Bk BT Italic

```html
<!DOCTYPE html>
<html lang="en">
<head>
<meta charset="utf-8">
<title>Sentrix business card – enlargement</title>
<link href="https://fonts.googleapis.com/css2?family=Jost:ital,wght@0,400;0,500;0,700;1,500&display=swap" rel="stylesheet">
<style>
  :root {
    --green: #1f4a2c;
    --red: #a1302a;
    --ink: #111111;
    --card: #ffffff;
    --stage-light: #f6f6f7;
    --stage-dark: #e6e6e8;
    --old-border: #d8d8d8;
  }
  * { margin: 0; padding: 0; box-sizing: border-box; }
  html, body { width: 1200px; height: 900px; overflow: hidden; }
  body {
    position: relative;
    font-family: "Jost", sans-serif;
    background: radial-gradient(ellipse at 40% 30%, var(--stage-light), var(--stage-dark));
  }
  .version-label {
    position: absolute;
    font-weight: 700;
    font-size: 27px;
    line-height: 1;
    color: var(--ink);
    letter-spacing: 0.02em;
  }
  .version-label--new { left: 810px; top: 22px; }
  .version-label--old { left: 235px; top: 296px; }

  .card {
    position: absolute;
    background: var(--card);
    border: 1px solid var(--green);
    overflow: hidden;
  }
  .card--old { left: 120px; top: 347px; width: 326px; height: 193px; font-size: 10.2px; border: 2px solid var(--old-border); }
  .card--new-small { left: 594px; top: 77px; width: 512px; height: 310px; font-size: 16px; }
  .card--new-large { left: 514px; top: 464px; width: 660px; height: 399px; font-size: 20.6px; }

  .brand-name {
    position: absolute;
    left: 1.55em; top: 2.95em;
    font-size: 2.95em;
    font-weight: 500;
    line-height: 1;
    color: var(--green);
    white-space: nowrap;
  }
  .brand-name { left: 0.53em; top: 1em; }
  .brand-square {
    position: absolute;
    left: 12.2em; top: 1.2em;
    width: 6.4em; height: 6.4em;
    background: var(--red);
  }
  .person-name {
    position: absolute;
    font-size: 1.6em;
    left: 11.56em; top: 6.06em;
    font-style: italic;
    font-weight: 500;
    line-height: 1;
    color: var(--red);
    white-space: nowrap;
  }
  .job-title {
    position: absolute;
    font-size: 1.07em;
    left: 17.38em; top: 10.9em;
    line-height: 1;
    color: var(--red);
    white-space: nowrap;
  }
  .contact-list {
    position: absolute;
    font-size: 1.17em;
    left: 1.25em; top: 10.1em;
    list-style: none;
    color: var(--green);
    line-height: 1.4;
    white-space: nowrap;
  }
</style>
</head>
<body>
  <div class="version-label version-label--new">NEW</div>
  <div class="version-label version-label--old">OLD</div>

  <div class="card card--old">
    <div class="brand-name">Sentrix</div>
    <div class="brand-square"></div>
    <div class="person-name">Morgan</div>
    <div class="job-title">Technical Operations</div>
    <ul class="contact-list">
      <li>T 03 4417</li><li>F 03 4417</li><li>D 03 4417</li>
      <li>www.sentrix.example</li>
    </ul>
  </div>

  <div class="card card--new-small">
    <div class="brand-name">Sentrix</div>
    <div class="brand-square"></div>
    <div class="person-name">Morgan</div>
    <div class="job-title">Technical Operations</div>
    <ul class="contact-list">
      <li>T 03 4417</li><li>F 03 4417</li><li>D 03 4417</li>
      <li>www.sentrix.example</li>
    </ul>
  </div>

  <div class="card card--new-large">
    <div class="brand-name">Sentrix</div>
    <div class="brand-square"></div>
    <div class="person-name">Morgan</div>
    <div class="job-title">Technical Operations</div>
    <ul class="contact-list">
      <li>T 03 4417</li><li>F 03 4417</li><li>D 03 4417</li>
      <li>www.sentrix.example</li>
    </ul>
  </div>
</body>
</html>
```